Flyer for "Learn to Brew Craft Beer" course

NEEDED: A6 flyer designed to advertise my first training course:
Intro to craft beer brewing

The company brand identity was recently bought from Pixel Harbour and it can be seen, with colour scheme on our website: www.TallowMashworks.com.

The flyer is to be in line with my current brand identity and have a strong hook to push people to our site.

The flyer's goal is to get people to visit the site to book on a craft beer brewing training course. The info available to be included, although you have the freedom to include as much or as little as you see fit:

Currently a sale of 60% off on the course cost
RRP £120 Sale Price £50 (limited time only)
Courses will be run in central London
The website is TallowMashworks.com
Hands on, half day course, brunch and a couple of sample beers included
Dates available:
14th December 2014
11th January 2015
18th January 2015
25th January 2015
1st February 2015
8th February 2015
15th February 2015
22nd February 2015

Logo file included, AI version available on request. Any photo on the TallowMashworks.com site is available to be used. Simply pull of the site or I can send to you.

Colour scheme used on site: #FF9700 & #26210D

I will reply to any designs offered between 8pm and 11pm BST each day.

Good luch!

Hi everyone, We have now reviewed the first submissions and there are some ok, some good and a couple of great efforts in there. Here are the following common things that we commented on in our first reviews: 1. WHAT IS THE FLYER TRYING TO SAY... YOU'VE GOT 1 SECOND!!!! This flyer is to be given out in the street. That gives you 1second to tell the reader what the flyer is selling. That is the number 1 priority for the flyer. Please make it your priority as designers. 2. SALE SALE SALE This is the number 2 priority, people love SALES and a big colourful sticker saying SALE or 60% OFF (or both) is to be positioned so once the reader has seen that the flyer is about a craft beer brewing course, they see there is a sale on the course. 3. BRAND PERSONALITY 3rd priority is the Tallow Mashworks brand identity. We picked this name, logo and colour scheme to stand out. Please use these to enhance points 1 & 2, but also get our logo on there is a bold and brash way. 4. USE THE BACK OF THE CARD Place any info that is not required in 1, 2 & 3 on the back, or even remove it all together if YOU feel it is not suited. You are the designer, so make some design decisions! We are happy to ask you to add things back in if we feel it is lacking. Our best guess (and we are NOT designers) is that putting either the dates OR a brief description of the course on the back would be enough info. If you think we can get bother, without overloading the page, give it a go! 5. CALL TO ACTION On the front and on the back, we want a CALL TO ACTION. Book at TallowMashworks.com or just TallowMashworks.com (you do not need http://www before it!!! We live in 2014 not 1994!!!) 6. MAKE IT BOLD, & THEN MAKE IT BOLDER This flyer is to stand out to a person that is handed 1 different leaflet every 2 minutes while walking down a busy London high street. We MUST stand out. Finally, thanks for all the designer so far, your efforts are greatly appreciated and we are very excited about the new revision of the design!

Target Market(s)

City living, young professionals who like to do fun things at the weekend.

Industry/Entity Type

Training

Font styles to use
Sans Serif

Colors
f78f20

Requirements
Must have
• Strong brand identity and call to action
In line with brand identity, see website www.TallowMashworks.com

```html
<!DOCTYPE html>
<html lang="en">
<head>
<meta charset="utf-8">
<title>Intro to Craft Beer Brewing – Tallow Mashworks Flyer</title>
<link href="https://fonts.googleapis.com/css2?family=Arimo:wght@400;700&display=swap" rel="stylesheet">
<style>
  :root {
    --amber: #f0a000;
    --amber-deep: #d98a00;
    --charcoal: #3a3838;
    --ink: #111111;
    --olive: #3b3517;
    --white: #ffffff;
    --stage: #efefef;
  }
  * { box-sizing: border-box; margin: 0; padding: 0; }
  html, body { width: 1200px; height: 1000px; overflow: hidden; }
  body {
    background: var(--stage);
    font-family: "Arimo", Arial, sans-serif;
    position: relative;
  }
  .flyer {
    position: absolute;
    left: 280px;
    width: 640px;
    height: 452px;
    overflow: hidden;
    box-shadow: 0 4px 16px rgba(0,0,0,.2);
  }
  .flyer--front { top: 30px; }
  .flyer--back { top: 518px; }

  /* shared */
  .photo { position: absolute; top: 0; right: 0; bottom: 0; }
  .brand-mark {
    position: absolute;
    display: flex; flex-direction: column; align-items: center; gap: 10px;
    font-weight: 700; font-size: 19px; line-height: 1.1; text-align: center;
    text-transform: uppercase; letter-spacing: 1px;
  }
  .brand-mark .dot { width: 54px; height: 54px; border-radius: 50%; }
  .kicker {
    position: absolute; display: flex; align-items: center; gap: 10px;
    font-weight: 700; font-size: 17px;
  }
  .kicker::before, .kicker::after { content: ""; height: 2px; width: 80px; }
  .headline {
    position: absolute; font-weight: 700; line-height: .95; text-align: center;
  }
  .subline {
    position: absolute; display: flex; align-items: center; gap: 26px;
    font-weight: 700;
  }
  .subline .star { width: 14px; height: 14px; }
  .band { position: absolute; left: 0; right: 0; }
  .band .url {
    position: absolute; font-weight: 700; letter-spacing: .5px; color: var(--white);
  }

  /* front */
  .flyer--front .photo {
    left: 183px;
    background: radial-gradient(ellipse at 60% 40%, #f6b733 0%, #e99a12 45%, #c77506 100%);
  }
  .flyer--front .side { position: absolute; left: 0; top: 0; width: 183px; height: 100%; background: var(--charcoal); }
  .flyer--front .brand-mark { left: 0; width: 183px; top: 70px; color: var(--white); }
  .flyer--front .brand-mark .dot { background: var(--white); }
  .flyer--front .kicker { left: 290px; top: 108px; color: var(--ink); }
  .flyer--front .kicker::before, .flyer--front .kicker::after { background: var(--white); }
  .flyer--front .headline {
    left: 183px; width: 457px; top: 140px; font-size: 60px; color: var(--white);
    text-shadow: 3px 3px 5px rgba(0,0,0,.55);
  }
  .flyer--front .subline { left: 280px; top: 292px; font-size: 28px; color: var(--ink); }
  .flyer--front .subline .star { fill: var(--white); }
  .more-info { position: absolute; left: 375px; top: 338px; font-weight: 700; font-size: 28px; color: var(--ink); }
  .more-info span { color: var(--white); font-size: 34px; }
  .flyer--front .band { top: 382px; height: 46px; background: var(--amber-deep); }
  .flyer--front .band .url { left: 245px; top: 12px; font-size: 19px; }
  .sale { position: absolute; left: 22px; top: 300px; color: var(--white); font-weight: 700; }
  .sale-figure { font-size: 58px; letter-spacing: -2px; line-height: 1; }
  .sale-figure .pct { font-size: 30px; vertical-align: 24px; color: var(--white); }
  .sale-figure .off { font-size: 32px; color: var(--amber); letter-spacing: 0; margin-left: -20px; }
  .sale-note { position: absolute; left: 22px; top: 374px; color: var(--ink); font-weight: 700; }
  .sale-note .small { font-size: 14px; display: block; line-height: 1; }
  .sale-note .big { font-size: 36px; line-height: .9; }
  .sale-note .tail { font-size: 14px; position: absolute; left: 112px; top: 46px; }

  /* back */
  .flyer--back .photo {
    left: 165px;
    background: linear-gradient(100deg, #2a2824 0%, #5c5a56 35%, #3a3935 60%, #7b7975 85%, #2f2e2a 100%);
  }
  .flyer--back .side { position: absolute; left: 0; top: 0; width: 165px; height: 100%; background: var(--amber-deep); }
  .flyer--back .brand-mark { left: 0; width: 165px; top: 130px; color: var(--olive); }
  .flyer--back .brand-mark .dot { background: var(--olive); }
  .flyer--back .kicker { left: 255px; top: 32px; color: var(--white); }
  .flyer--back .kicker::before, .flyer--back .kicker::after { background: var(--white); }
  .flyer--back .headline { left: 250px; top: 56px; font-size: 50px; color: var(--amber); text-align: left; }
  .flyer--back .subline { left: 260px; top: 160px; font-size: 25px; color: var(--white); }
  .flyer--back .subline .star { fill: var(--white); }
  .rule { position: absolute; left: 255px; top: 196px; width: 373px; height: 2px; background: var(--white); }
  .pricing { position: absolute; left: 165px; width: 475px; top: 212px; color: var(--white); text-align: center; font-size: 15px; line-height: 1.4; }
  .dates { position: absolute; left: 180px; top: 272px; color: var(--white); display: flex; gap: 20px; }
  .dates .col { line-height: 1.15; }
  .dates .year { font-size: 18px; }
  .dates .month { font-size: 15px; font-weight: 700; }
  .dates .days { font-size: 22px; }
  .dates .first { text-align: right; }
  .dates .divider { width: 2px; background: var(--white); height: 66px; margin-top: 2px; }
  .dates .row { display: flex; align-items: baseline; gap: 4px; }
  .flyer--back .band { top: 390px; height: 36px; background: var(--olive); }
  .flyer--back .band .url { left: 270px; top: 9px; font-size: 16px; }
</style>
</head>
<body>

<section class="flyer flyer--front" aria-label="Flyer front">
  <div class="photo" role="img" aria-label="Close-up photograph of golden beer with rising bubbles"></div>
  <div class="side"></div>
  <div class="brand-mark"><span class="dot"></span>Tallow<br>Mashworks</div>
  <div class="kicker">Intro to</div>
  <h1 class="headline">Craft Beer<br>BREWING</h1>
  <div class="subline">
    <svg class="star" viewBox="0 0 24 24"><polygon points="12,1 15,9 23,9 17,14 19,22 12,17 5,22 7,14 1,9 9,9"/></svg>
    training course
    <svg class="star" viewBox="0 0 24 24"><polygon points="12,1 15,9 23,9 17,14 19,22 12,17 5,22 7,14 1,9 9,9"/></svg>
  </div>
  <div class="more-info"><span>+</span>info</div>
  <div class="band"><span class="url">www.TallowMashworks.com</span></div>
  <div class="sale"><div class="sale-figure">60<span class="pct">%</span><span class="off">off</span></div></div>
  <div class="sale-note"><span class="small">on</span><span class="big">course</span><span class="tail">cost</span></div>
</section>

<section class="flyer flyer--back" aria-label="Flyer back">
  <div class="photo" role="img" aria-label="Dim photograph of stainless steel beer taps"></div>
  <div class="side"></div>
  <div class="brand-mark"><span class="dot"></span>Tallow<br>Mashworks</div>
  <div class="kicker">Intro to</div>
  <h2 class="headline">Craft Beer<br>BREWING</h2>
  <div class="subline">
    <svg class="star" viewBox="0 0 24 24"><polygon points="12,1 15,9 23,9 17,14 19,22 12,17 5,22 7,14 1,9 9,9"/></svg>
    training course
    <svg class="star" viewBox="0 0 24 24"><polygon points="12,1 15,9 23,9 17,14 19,22 12,17 5,22 7,14 1,9 9,9"/></svg>
  </div>
  <div class="rule"></div>
  <p class="pricing">RRP £120 Sale Price £50 <strong>(limited time only)</strong><br>Courses will be run in central London</p>
  <div class="dates">
    <div class="col first">
      <div class="year">2014</div>
      <div class="month">December</div>
      <div class="days">14th</div>
    </div>
    <div class="divider"></div>
    <div class="col">
      <div class="year">2015</div>
      <div class="row"><span class="month">January</span><span class="days">11th /18th /25th</span></div>
      <div class="row"><span class="month">February</span><span class="days">1st /8th /15th /22th</span></div>
    </div>
  </div>
  <div class="band"><span class="url">www.TallowMashworks.com</span></div>
</section>

</body>
</html>
```